1/4 page print add needed for local government consultancy entering new line of business.

We need a 1/4 page print ad for a trade conference program (Live Area of 3.75"x5") to help roll out a new consulting product intended for local governments in Texas. Our Bond Rating Assessment helps cities to maximize their Bond Rating and financial efficiency by lowering overall cost of debt-financed projects. Our audience is generally conservative and professional and about 90% male. Our company is the KVMorrow Partners, LLC and I have attached our logo. We generally use bright blue tones, greys, and black in our other marketing material. Ad should cause people to go to www.kvmorrowpartners.example to get more information. Final product needs to be either PDF or JPEG at a minimum resolution of 300dpi.

After seeing some of the initial designs, I realize that while I want to highlight the Bond Rating Assessments, I need some more information about my business in the ad. I would also like to include a brief mention (probably title only) of my other lines of service: Economic Development Consulting, Executive Dashboards, Strategic Planning & Performance Management, Public Policy Analysis, and Governance Training. Thanks!

Target Market(s)

Highly educated professional public servants (City Managers). Generally stylistically conservative. Ad will run only in Texas, USA.

Industry/Entity Type

Government

Font styles to use
Sans Serif

Colors
0792cd

Requirements
Must have
• 1. Brief Description of Bond Rating Assessment service.
• 2. Call to action to visit www.kvmorrowpartners.example for more information.
• 3. Company logo (see attached)

```html
<!DOCTYPE html>
<html lang="en">
<head>
<meta charset="utf-8">
<title>KVMorrow Partners – Bond Rating Assessment</title>
<link rel="stylesheet" href="https://fonts.googleapis.com/css2?family=Montserrat:wght@800&family=Nunito+Sans:wght@400;700;800&display=swap">
<style>
  :root {
    --blue-deep: #0a4f88;
    --blue-mid: #0b6fb0;
    --blue-bright: #1ba3df;
    --brand-blue: #0792cd;
    --sky: #5ccbf5;
    --gold: #f5c118;
    --white: #ffffff;
    --paper: #ffffff;
    --ink-grey: #4a4a4a;
  }
  * { margin: 0; padding: 0; box-sizing: border-box; }
  html, body { width: 865px; height: 1200px; overflow: hidden; background: var(--paper); }
  .ad {
    position: relative;
    width: 865px;
    height: 1200px;
    font-family: "Nunito Sans", Arial, sans-serif;
  }
  .hero {
    position: absolute;
    left: 0; top: 0;
    width: 865px; height: 1003px;
    overflow: hidden;
    background: radial-gradient(ellipse 75% 60% at 58% 58%, var(--blue-bright) 0%, var(--blue-mid) 55%, var(--blue-deep) 100%);
  }
  .growth-visual {
    position: absolute;
    left: 0; top: 660px;
    width: 865px; height: 343px;
    background: linear-gradient(20deg, rgba(245,193,24,0.28) 0%, rgba(30,109,176,0.35) 55%, rgba(27,163,223,0) 100%);
  }
  .headline {
    position: absolute;
    left: 69px; top: 110px;
    font-family: "Montserrat", Arial, sans-serif;
    font-weight: 800;
    color: var(--sky);
    line-height: 1;
    text-transform: uppercase;
  }
  .headline .lead { display: block; font-size: 50px; letter-spacing: 0.5px; }
  .headline .main { display: block; font-size: 79px; margin-top: 2px; letter-spacing: 0.5px; }
  .subhead {
    position: absolute;
    left: 69px; top: 266px;
    width: 760px;
    font-weight: 800;
    font-size: 28px;
    line-height: 38px;
    color: var(--white);
  }
  .subhead .highlight { color: var(--gold); }
  .description {
    position: absolute;
    left: 69px; top: 372px;
    width: 740px;
    font-size: 22px;
    line-height: 36.5px;
    color: var(--white);
  }
  .description strong { font-weight: 800; }
  .call-to-action {
    position: absolute;
    right: 73px; top: 922px;
    text-align: right;
    font-weight: 800;
    font-size: 22px;
    line-height: 34px;
    color: var(--white);
  }
  .footer {
    position: absolute;
    left: 0; top: 1003px;
    width: 865px; height: 197px;
    background: var(--paper);
  }
  .brand-name {
    position: absolute;
    left: 69px; top: 42px;
    display: flex;
    align-items: center;
    gap: 14px;
    font-weight: 700;
    font-size: 30px;
    line-height: 1.1;
    color: var(--ink-grey);
  }
  .brand-name .mark {
    width: 22px; height: 22px;
    background: var(--ink-grey);
    flex: none;
  }
  .contact {
    position: absolute;
    right: 73px; top: 36px;
    text-align: right;
    font-style: normal;
    color: var(--brand-blue);
    font-size: 26px;
    line-height: 36px;
  }
  .contact .website { font-weight: 800; font-size: 29px; margin-top: 2px; }
</style>
</head>
<body>
<main class="ad">
  <section class="hero">
    <div class="growth-visual" role="img" aria-label="Rising gold and blue line chart with circular markers and arrowheads showing improving bond ratings"></div>

    <h1 class="headline">
      <span class="lead">Confused about</span>
      <span class="main">Bond Ratings?</span>
    </h1>
    <p class="subhead">Our Assessment delivers the tools you need to<br><span class="highlight">maximize your community's Bond Ratings.</span></p>
    <p class="description">At <strong>KVMorrow Partners, LLC</strong>, our Bond Rating Assessment will<br>provide you a detailed report on what the agencies are looking<br>at, what their red flags may be, and we will provide advice on<br>how to best communicate your community's strengths to the<br>analysts to ensure that you get the highest rating possible given<br>your underlying financials. Then, we help prepare you and your<br>financial team for the ratings calls, showing you exactly what to<br>highlight as you represent the community.</p>
    <p class="call-to-action">If you are ready to maximize<br>your Bond Rating, contact us at:</p>
  </section>

  <footer class="footer">
    <div class="brand-name"><span class="mark"></span><span>KVMorrow<br>Partners, LLC</span></div>
    <address class="contact">
      <div class="phone">Tel.: (555) 014-2730</div>
      <div class="email">info@kvmorrowpartners.example</div>
      <div class="website">www.kvmorrowpartners.example</div>
    </address>
  </footer>
</main>
</body>
</html>
```